Book jacket for Drumlore

We need a book jacket design (hard cover front, back, spine, flaps; soft cover and eBook). for a social psychology book with the general cluelessness (being "out of it") of how people function both in their personal and social lives. This is the third book written by the author, a practicing psychiatrist, and the content centers on a single subject, people's lack of genuine emotional contact, their cluelessness with themselves and with current national and world events.

Target Market(s)

People who want to better understand the state the nation and world is in now, and what they can do about it.

Font styles to use
Serif
Sans Serif

Requirements
Must have
• Bold, eye-catching cover
Nice to have
• Like the idea of separating the title word (drum lore) to better emphasize the concept of lack of contact

```html
<!DOCTYPE html>
<html lang="en">
<head>
<meta charset="utf-8">
<title>Drumlore — Book Jacket Front</title>
<link rel="stylesheet" href="https://fonts.googleapis.com/css2?family=Oswald:wght@400;700&display=swap">
<style>
  :root {
    --paper: #ffffff;
    --title-grey: #959695;
    --title-red: #aa1f23;
    --author-ink: #2b2b2b;
    --swarm-dark: #5a2a1a;
    --swarm-warm: #a5582c;
  }
  html, body {
    margin: 0;
    padding: 0;
    overflow: hidden;
    background: var(--paper);
  }
  .cover {
    position: relative;
    width: 840px;
    height: 1200px;
    background: var(--paper);
    overflow: hidden;
  }
  .swarm {
    position: absolute;
    left: 0;
    top: 0;
    width: 720px;
    height: 520px;
  }
  .stray {
    position: absolute;
    left: 645px;
    top: 872px;
    width: 56px;
    height: 56px;
  }
  .title {
    position: absolute;
    left: 0;
    top: 0;
    width: 840px;
    height: 820px;
  }
  .title text {
    font-family: "Oswald", "Arial Narrow", sans-serif;
    font-weight: 700;
    font-size: 290px;
  }
  .title .word-top { fill: var(--title-grey); }
  .title .word-bottom { fill: var(--title-red); }
  .author {
    position: absolute;
    left: 0;
    width: 840px;
    top: 1098px;
    margin: 0;
    text-align: center;
    font-family: "Oswald", "Arial Narrow", sans-serif;
    font-weight: 400;
    font-size: 50px;
    line-height: 1;
    color: var(--author-ink);
  }
</style>
</head>
<body>
<div class="cover">
  <svg class="swarm" viewBox="0 0 720 520" role="img" aria-label="Photograph of a scattered swarm of small red-brown ants spreading across the upper left of the cover">
    <defs>
      <radialGradient id="swarmTone" cx="0.35" cy="0.3" r="0.75">
        <stop offset="0" stop-color="var(--swarm-warm)" stop-opacity="0.28"/>
        <stop offset="0.6" stop-color="var(--swarm-dark)" stop-opacity="0.14"/>
        <stop offset="1" stop-color="var(--swarm-dark)" stop-opacity="0"/>
      </radialGradient>
    </defs>
    <path d="M0 0 H720 C700 120 600 220 470 260 C360 300 300 330 200 360 C150 380 140 460 110 510 L0 510 Z" fill="url(#swarmTone)"/>
  </svg>

  <svg class="stray" viewBox="0 0 56 56" role="img" aria-label="Photograph of a single ant wandering alone">
    <defs>
      <radialGradient id="strayTone">
        <stop offset="0" stop-color="var(--swarm-dark)" stop-opacity="0.35"/>
        <stop offset="1" stop-color="var(--swarm-dark)" stop-opacity="0"/>
      </radialGradient>
    </defs>
    <circle cx="28" cy="28" r="28" fill="url(#strayTone)"/>
  </svg>

  <svg class="title" viewBox="0 0 840 820" aria-label="Drumlore">
    <text class="word-top" x="167" y="570" textLength="499" lengthAdjust="spacingAndGlyphs">DRUM</text>
    <text class="word-bottom" x="198" y="797" textLength="462" lengthAdjust="spacingAndGlyphs">LORE</text>
  </svg>

  <p class="author">Martin Aldous M.D</p>
</div>
</body>
</html>
```